CD Cover -Vekko - Copperwing (ft. Tiri Jal)

We need a CD Cover immediately. We are dissatisfied with our past and wish that someone can help us.

Teamed's "Copperwing" as single units as you can see, this template I sent to where you see the text that will be with.

We hope that you can help us with this promptly. We are looking for someone who is creative and can do anything on their own.

Industry/Entity Type

Music Download

Font styles to use
Decorative

Requirements
Must have
• Änvänd er kreativitet och gör det ni tror hade passat?
Nice to have
• Copperwing Cartoon jus
• 1400x1400
Should not have
• Copperwing

```html
<!DOCTYPE html>
<html lang="en">
<head>
<meta charset="utf-8">
<title>Vekko feat. Tiri Jal – Copperwing</title>
<link href="https://fonts.googleapis.com/css2?family=Luckiest+Guy&display=block" rel="stylesheet">
<style>
  :root {
    --teal: #2e9880;
    --teal-light: #3aa88f;
    --yellow: #e4e83a;
    --yellow-shade: #c9b82a;
    --pink: #d84f9c;
    --pink-shade: #a9457e;
    --ink: #0b0b0b;
    --splash-warm: #6b5432;
    --splash-mid: #2a2217;
  }
  html, body {
    margin: 0;
    padding: 0;
    width: 1200px;
    height: 1200px;
    overflow: hidden;
    background: var(--teal);
  }
  .cover {
    position: relative;
    width: 1200px;
    height: 1200px;
    background: radial-gradient(circle at 50% 50%, var(--teal-light), var(--teal) 75%);
    overflow: hidden;
  }
  .artwork {
    position: absolute;
    inset: 0;
    display: block;
  }
  .title-text {
    font-family: "Luckiest Guy", "Arial Black", "Impact", sans-serif;
    font-weight: 400;
    fill: var(--ink);
    stroke: var(--ink);
    stroke-width: 3px;
    stroke-linejoin: round;
  }
  .artist-line { font-size: 104px; }
  .song-title { font-size: 212px; }
</style>
</head>
<body>
<main class="cover">
  <svg class="artwork" width="1200" height="1200" viewBox="0 0 1200 1200">
    <defs>
      <radialGradient id="splash-glow" cx="0.5" cy="0.5" r="0.45">
        <stop offset="0" stop-color="var(--splash-warm)"/>
        <stop offset="0.55" stop-color="var(--splash-mid)"/>
        <stop offset="1" stop-color="#000"/>
      </radialGradient>
    </defs>

    <polygon class="band-yellow-shade" points="56,58 1158,58 1158,362 56,386" fill="var(--yellow-shade)"/>
    <polygon class="band-yellow" points="54,50 1158,52 1157,352 54,380" fill="var(--yellow)"/>

    <g role="img" aria-label="Photo of a champagne cork flying out with a spray of golden sparkling wine on black">
      <polygon class="band-photo" points="50,428 1158,393 1158,772 44,734" fill="#000"/>
      <ellipse cx="600" cy="580" rx="460" ry="140" fill="url(#splash-glow)"/>
    </g>

    <polygon class="band-pink-shade" points="45,774 1158,790 1158,800 45,784" fill="var(--pink-shade)"/>
    <polygon class="band-pink" points="44,782 1158,798 1158,1152 44,1150" fill="var(--pink)"/>

    <text class="title-text artist-line" x="86" y="244" textLength="1030" lengthAdjust="spacingAndGlyphs">VEKKO FEAT. TIRI JAL</text>
    <text class="title-text song-title" x="96" y="1064" textLength="1008" lengthAdjust="spacingAndGlyphs">COPPERWING</text>
  </svg>
</main>
</body>
</html>
```